Church Lanterns Over Millbrook Gospel Booklet Design

We need a booklet designed that we will be printing to hand out in our community. Wording for each page will be provided and we need graphic design to produce the layouts in a format ready for print. Booklet will be 4.75" x 4.75" square and a total of 12 pages: 1 cover page front, 1 cover page back, 10 inside pages some of which will be full spread across 2 pages.

Target Market(s)

English speaking Westerners

Industry/Entity Type

Religious

Font styles to use
Serif

Colors
ffffff
85abd2
0292cd
33b8a4
5c5c5c

Requirements
Must have
• Minimalist design with clean look described in attached document
Nice to have
• Aesthetically pleasing graphics, crisp fonts, excellent turn around times
Should not have
• Effeminate design, busy look with too much graphic and text

```html
<!DOCTYPE html>
<html lang="en">
<head>
<meta charset="UTF-8">
<title>Lanterns Over Millbrook — Salvation Spread</title>
<link rel="stylesheet" href="https://fonts.googleapis.com/css2?family=Nunito:wght@800&family=Libre+Baskerville&display=swap">
<style>
  :root {
    --paper: #ffffff;
    --soft-blue: #85abd2;
    --quote-blue: #8fb2d6;
    --sky: #f3f7fb;
    --haze: #dfeaf4;
    --sea-light: #9cc6e6;
    --sea: #6aa4d2;
    --sea-deep: #3a78ae;
  }
  html, body {
    margin: 0;
    padding: 0;
    overflow: hidden;
    background: var(--paper);
  }
  .spread {
    position: relative;
    width: 1200px;
    height: 600px;
    display: flex;
    overflow: hidden;
    background: var(--paper);
  }
  .page-text {
    position: relative;
    width: 595px;
    height: 600px;
    box-sizing: border-box;
  }
  .salvation-heading {
    position: absolute;
    top: 120px;
    left: 0;
    width: 595px;
    margin: 0;
    text-align: center;
    font-family: "Nunito", sans-serif;
    font-weight: 800;
    font-size: 17px;
    letter-spacing: 0.6px;
    color: var(--soft-blue);
  }
  .salvation-steps {
    position: absolute;
    top: 178px;
    left: 72px;
    width: 450px;
    margin: 0;
    text-align: center;
    font-family: "Nunito", sans-serif;
    font-weight: 800;
    font-size: 19px;
    line-height: 23.3px;
    color: var(--soft-blue);
  }
  .scripture {
    position: absolute;
    top: 438px;
    left: 72px;
    width: 452px;
    margin: 0;
    text-align: center;
    font-family: "Libre Baskerville", serif;
    font-size: 13.5px;
    line-height: 23.5px;
    color: var(--quote-blue);
  }
  .scripture cite {
    display: block;
    font-style: normal;
  }
  .page-photo {
    width: 605px;
    height: 600px;
    background:
      linear-gradient(180deg,
        var(--sky) 0%,
        var(--haze) 22%,
        var(--sea-light) 28%,
        var(--sea) 60%,
        var(--sea-deep) 100%);
  }
</style>
</head>
<body>
  <main class="spread">
    <section class="page-text">
      <h1 class="salvation-heading">Here is what you must do to be saved:</h1>
      <p class="salvation-steps">First, ask the Shepherd to save you (Since he is God, he can hear you): Acknowledge that God is the rightful authority of the universe and your life. Apologize to him for your rebellion against God. Ask the Shepherd to come into your life as your Lord and Savior. This decision will immediately trigger his miracle of salvation in you. God now lives in you!</p>
      <blockquote class="scripture">“If you confess with your mouth that the Shepherd is Lord and believe in your heart that God raised him from the dead, you will be saved.”<cite>(Romans 10:9)</cite></blockquote>
    </section>
    <div class="page-photo" role="img" aria-label="Photo of an open hand reaching out toward a sunlit, sparkling blue sea under a pale sky"></div>
  </main>
</body>
</html>
```